Red Kettle Handcrafted Tomato Ketchup packaging design modern

From the best ingredients there is the best ketchup Red Handcrafted ketchup are specially formulated for fine dining and drinks, bringing out all the flavors. As the Red Kettle handcrafted ketchup is otherwise fabulous: Made with wholesome, fully ripe fruits Nothing with half things! All Red Kettle handcrafted ketchups are pure nature, without any artificial diluents or concentrates. Where tomato is on it, that's all there is to it - guaranteed! the design should be professional and noble despite being trendy. A watcher wants to sell the ketchup as merchandising from our restaurant. but as a single brand positioning. The ketchup is vegan. Dimensions: 6.8 cm Height: 7.8 cm Circumference: 21.6 cm The text down (Text 1-4). The lid of the text the glass packaging is black! Thanks for your efforts. I look forward to your designs.

Target Market(s)

foodies

Font styles to use
Serif
Sans Serif

Colors

Designer to choose colors to be used in the design.

Requirements
Must have
• Title: (Handcrafted Tomato Ketchup) Text One: (Store chilled after opening and consume quickly, pasteurized.) Text Two: (Handcrafted in Switzerland by Brentwick Gastro GmbH, Chur www.redkettle-example.ch) Text Tree: (Tomatoes, White Wine Vinegar, Aceto Balsamico, Brown Cane Sugar, Corn Starch, Spices, Salt) Text For: (200 grams) or (200g) The Logo of Red Kettle with the Pasta and Wine have to because of the gesety.
Nice to have
• small vegan icon (maybe)
Should not have
• text of the logo (pasta & wine)

```html
<!DOCTYPE html>
<html lang="de">
<head>
<meta charset="utf-8">
<title>Red Kettle – Handcrafted Tomato Ketchup Label</title>
<link rel="stylesheet" href="https://fonts.googleapis.com/css2?family=Cinzel:wght@700;900&family=Montserrat:wght@500;600;700&display=swap">
<style>
  :root {
    --paper: #ffffff;
    --backdrop: #ffffff;
    --gold: #e2a862;
    --gold-soft: #f0c995;
    --ketchup-red: #d42a2a;
    --tomato-light: #f0533a;
    --tomato-dark: #b8160f;
    --ink: #2b2b2b;
    --pill: #e9b877;
  }
  * { box-sizing: border-box; margin: 0; padding: 0; }
  html, body {
    width: 1200px; height: 596px; overflow: hidden;
    background: var(--backdrop);
  }
  .canvas { position: relative; width: 1200px; height: 596px; }

  .label {
    position: absolute; top: 232px; width: 362px; height: 262px;
    background: var(--paper);
    box-shadow: 0 0 0 1px #eee;
  }
  .label--front { left: 188px; }
  .label--back { left: 664px; }

  .label__trim { position: absolute; left: 0; width: 100%; height: 10px; }
  .label__trim--top { top: 4px; border-top: 2px dotted var(--gold); border-bottom: 2px solid var(--gold); }
  .label__trim--bottom { bottom: 4px; border-bottom: 2px dotted var(--gold); border-top: 2px solid var(--gold); }

  /* Front */
  .brand {
    position: absolute; left: 0; top: 78px; width: 100%;
    text-align: center;
    font-family: "Montserrat", sans-serif; font-weight: 600;
    font-size: 15px; letter-spacing: 4px; color: var(--ink);
  }
  .brand__dot {
    display: inline-block; width: 7px; height: 7px; border-radius: 50%;
    background: var(--gold); vertical-align: middle; margin-right: 8px;
  }
  .product-title { position: absolute; left: 0; top: 124px; width: 100%; text-align: center; color: var(--ketchup-red); }
  .product-title__sub {
    display: block; font-family: "Montserrat", sans-serif; font-weight: 700;
    font-size: 8.5px; letter-spacing: 3.2px;
  }
  .product-title__main {
    display: block; font-family: "Cinzel", serif; font-weight: 900;
    font-size: 40px; line-height: 40px; letter-spacing: 1px;
  }
  .tomato-art {
    position: absolute; left: 86px; top: 180px; width: 188px; height: 64px;
    border-radius: 50% 50% 46% 46%;
    background: radial-gradient(ellipse at 40% 45%, var(--tomato-light), var(--ketchup-red) 60%, var(--tomato-dark));
  }

  /* Back */
  .info { position: absolute; left: 28px; right: 20px; font-family: "Montserrat", sans-serif; font-weight: 500; font-size: 12.5px; line-height: 14px; letter-spacing: 1px; color: var(--ink); }
  .info--storage { top: 34px; }
  .info--maker { top: 94px; }
  .info--ingredients { top: 152px; }
  .info__web { color: var(--ketchup-red); font-weight: 700; }
  .divider { position: absolute; left: 24px; right: 24px; height: 2px; background: linear-gradient(90deg, transparent, var(--gold) 20%, var(--gold) 80%, transparent); }
  .divider--one { top: 84px; }
  .divider--two { top: 142px; }
  .weight {
    position: absolute; left: 120px; top: 218px; width: 122px; height: 24px;
    border-radius: 12px; background: var(--pill); border: 1px solid var(--gold);
    text-align: center; line-height: 22px;
    font-family: "Montserrat", sans-serif; font-weight: 700; font-size: 15px; letter-spacing: 1px; color: var(--ketchup-red);
  }
</style>
</head>
<body>
<main class="canvas">
  <section class="label label--front">
    <div class="label__trim label__trim--top"></div>
    <p class="brand"><span class="brand__dot"></span>RED KETTLE</p>
    <h1 class="product-title">
      <span class="product-title__sub">HANDCRAFTED TOMATO</span>
      <span class="product-title__main">KETCHUP</span>
    </h1>
    <div class="tomato-art" role="img" aria-label="Photo of ripe red tomatoes, one cut in half"></div>
    <div class="label__trim label__trim--bottom"></div>
  </section>

  <section class="label label--back">
    <div class="label__trim label__trim--top"></div>
    <p class="info info--storage">Nach dem Öffnen gekühlt aufbewahren und rasch konsumieren. Pasteurisiert.</p>
    <div class="divider divider--one"></div>
    <p class="info info--maker">Handcrafted in Switzerland by Brentwick Gastro GmbH, Chur<br><span class="info__web">www.redkettle-example.ch</span></p>
    <div class="divider divider--two"></div>
    <p class="info info--ingredients">Tomaten, Weissweinessig, Aceto Balsamico, brauner Rohrzucker, Maisstärke, Gewürze, Salz</p>
    <p class="weight">200g</p>
    <div class="label__trim label__trim--bottom"></div>
  </section>
</main>
</body>
</html>
```